Website refresh! Software products and services.
B2B site: 3 page templates, Well thought out requirements, brief and some wireframes
Website refresh! Software products and services. - Information Technology
Creative Brief
Information Technology
www.qnr.co.nz
QNR is a software company focussed on Operations Management and Operations Intelligence systems for Utilities (Elec, Gas, Water), Transport/Logistics companies, and Radio network users. We have been in business for 10+ years and have clients all over the world. Our products are robust, credible, and meet the needs of these customers.
This is a B2B site. Needs to be clean and easy to navigate, information, screen shots, relevant graphics. Refer to the attached preliminary design brief.
High Tech
Red banner
Blue
Arial, Verdana, Trebuchet MS, Times New Roman, Century Gothic, Georgia
left side
www.larkmoorco.com
http://www.7jq.com
http://www.vo-powerline.com/products_and_services/products/utility_operations_software/
CMS will be wordpress. 3 page Templates and associated graphics. 1. Home/Landing page 2. Inside Category and Product Pages 3. Miscellaneous pages, eg Contact Us, Careers, News & Events, etc. Refer to the attached Summary design brief which has example sites, UI ideas, Wireframes of suggested page layout. Copy will also be provided to the selected designer so they can see how the content will fit with design.

```html
<!DOCTYPE html>
<html lang="en">
<head>
<meta charset="utf-8">
<title>QNR – Operations Management Software</title>
<link href="https://fonts.googleapis.com/css2?family=Arimo:wght@400;700&family=Open+Sans:wght@300;400;600;700&display=swap" rel="stylesheet">
<style>
  :root{
    --ink:#333;
    --muted:#777;
    --light:#999;
    --rule:#dcdcdc;
    --bar:#2e2e2e;
    --bar-text:#bbb;
    --accent-red:#d8312a;
    --accent-green:#3ba34a;
    --panel:#f4f4f4;
    --white:#fff;
  }
  *{box-sizing:border-box;margin:0;padding:0}
  ul{list-style:none}
  html,body{width:1200px;height:1096px;overflow:hidden;background:var(--white)}
  body{font-family:"Arimo",Arial,sans-serif;color:var(--ink);font-size:12px;position:relative}

  .top-bar{height:24px;background:var(--bar);display:flex;align-items:center;justify-content:space-between;padding:0 125px;font-size:10px;color:var(--bar-text)}
  .top-bar nav{display:flex;gap:14px}
  .top-bar nav a:first-child{color:var(--white);font-weight:700}
  .top-bar a{color:var(--bar-text);text-decoration:none}
  .follow{display:flex;gap:6px;align-items:center}
  .follow b{color:var(--white)}
  .lang{margin-left:22px;color:var(--white);font-weight:700}

  .masthead{position:absolute;top:56px;left:125px;width:950px;height:60px}
  .brand{display:flex;align-items:center;gap:12px;font-family:"Open Sans",sans-serif;font-weight:700;font-size:44px;letter-spacing:6px;color:#222}
  .brand .dot{width:32px;height:32px;border-radius:50%;background:var(--accent-red)}
  .search{position:absolute;right:0;top:0;display:flex;gap:4px}
  .search .field{width:120px;height:20px;border:1px solid var(--rule);font-size:9px;color:var(--light);padding:4px 6px}
  .search .btn{height:20px;padding:4px 8px;border:1px solid var(--rule);background:var(--panel);font-size:9px;color:var(--muted)}

  .main-nav{position:absolute;top:120px;left:125px;width:950px;border-bottom:1px solid var(--rule);display:flex;justify-content:flex-end;gap:26px;padding-bottom:8px;font-size:13px}
  .main-nav a{color:var(--ink);text-decoration:none}
  .main-nav a.current{color:var(--muted)}
  .main-nav .caret{font-size:9px}

  .hero{position:absolute;top:172px;left:125px;width:950px;height:306px;display:flex}
  .hero-photo{width:680px;height:100%;background:linear-gradient(180deg,#6f9fd0 0%,#a9c8e6 55%,#dfe8d0 72%,#c9c243 80%,#a4a23a 100%);position:relative}
  .hero-caption{position:absolute;left:24px;bottom:26px;background:rgba(240,240,240,.9);padding:10px 14px;width:270px;font-size:11px;line-height:16px;color:#444}
  .solutions{width:270px;display:flex;flex-direction:column}
  .solution{flex:1;border-bottom:1px solid #bdbdbd;background:linear-gradient(180deg,#d9d9d9,#c4c4c4);display:flex;align-items:center;gap:10px;padding:0 10px}
  .solution:first-child{background:linear-gradient(180deg,#ececec,#d6d6d6)}
  .solution .icon{flex:none;width:22px;height:22px;border-radius:50%;background:var(--white);border:5px solid var(--accent-red)}
  .solution:nth-child(even) .icon{border-color:var(--accent-green)}
  .solution h3{font-size:11px;font-weight:700;color:#333}
  .solution p{font-size:9px;color:#666;line-height:12px}

  .columns{position:absolute;top:512px;left:125px;width:950px;display:flex;border:1px solid var(--rule);height:306px}
  .col{padding:12px 16px}
  .col.featured{width:350px;border-right:1px solid var(--rule)}
  .col.about{width:310px;border-right:1px solid var(--rule)}
  .col.news{flex:1}
  .col h2{font-family:"Open Sans",sans-serif;font-weight:300;font-size:18px;letter-spacing:1px;color:#555;padding-bottom:8px;border-bottom:1px solid var(--rule);margin-bottom:12px;text-transform:uppercase}
  .feature-photo{width:254px;height:90px;background:linear-gradient(180deg,#4c8fd6 0%,#8ec3ee 45%,#2f5f9a 55%,#6aa4d6 70%,#b9c640 85%,#8a9c2b 100%);margin-bottom:8px}
  .col p{font-size:10px;line-height:15px;color:var(--muted)}
  .quote{font-weight:700;color:#444 !important;margin-bottom:10px;padding-left:10px;position:relative}
  .quote::before{content:"\201C";position:absolute;left:-2px;top:-4px;font-size:18px;color:#444}
  .news-list{position:relative;padding-left:22px;height:236px}
  .news-list .item{margin-bottom:10px}
  .news-list time{display:block;font-size:9px;color:var(--light)}
  .arrow{position:absolute;left:0;width:16px;height:16px;border-radius:50%;background:#e6e6e6;border:1px solid #ccc}
  .arrow svg{display:block;margin:4px auto}
  .arrow.up{top:0}
  .arrow.down{top:216px}

  .partners{position:absolute;top:840px;left:125px;width:950px;height:66px;border:1px solid var(--rule);display:flex;align-items:center;justify-content:space-around}
  .partner{display:flex;align-items:center;gap:6px;font-weight:700;font-size:15px;color:#444;letter-spacing:1px}
  .partner .mark{width:10px;height:10px;background:#444}

  .footer{position:absolute;top:956px;left:125px;font-size:10px;color:var(--light)}
</style>
</head>
<body>
  <header class="top-bar">
    <nav><a href="#">Home</a><a href="#">Featured</a><a href="#">What's New?</a><a href="#">Specials</a><a href="#">Reviews</a><a href="#">Contact</a></nav>
    <div class="follow">Follow us on: <b>Chirpline</b> <b>Pagefold</b> and <b>Shotboard</b><span class="lang">En</span></div>
  </header>

  <div class="masthead">
    <div class="brand"><span class="dot"></span>QNR</div>
    <div class="search"><div class="field">Enter keyword here</div><div class="btn">Search</div></div>
  </div>

  <nav class="main-nav">
    <a href="#" class="current">Home</a>
    <a href="#">Product Solutions <span class="caret">▼</span></a>
    <a href="#">Partners</a>
    <a href="#">News&amp;Events</a>
    <a href="#">Careers</a>
    <a href="#">About QNR</a>
    <a href="#">Contacts</a>
  </nav>

  <section class="hero">
    <div class="hero-photo" role="img" aria-label="Wind turbines on a green and yellow field under a blue sky">
      <div class="hero-caption">Complete in and Outbound communications<br>Going live at supply</div>
    </div>
    <ul class="solutions">
      <li class="solution"><span class="icon"></span><div><h3>Timeline Call Management</h3><p>Nunc id tempus ante, commodo eleifend ante ligula.</p></div></li>
      <li class="solution"><span class="icon"></span><div><h3>Outage, Ops &amp; Works Mgt</h3><p>Nunc id tempus ante, commodo eleifend ante ligula.</p></div></li>
      <li class="solution"><span class="icon"></span><div><h3>Enterprise Grade IVR</h3><p>Nunc id tempus ante, commodo eleifend ante ligula.</p></div></li>
      <li class="solution"><span class="icon"></span><div><h3>Radio Users</h3><p>Nunc id tempus ante, commodo eleifend ante ligula.</p></div></li>
      <li class="solution"><span class="icon"></span><div><h3>Field Crew Solutions</h3><p>Nunc id tempus ante, commodo eleifend ante ligula.</p></div></li>
    </ul>
  </section>

  <section class="columns">
    <article class="col featured">
      <h2>Featured</h2>
      <div class="feature-photo" role="img" aria-label="Solar panels in a sunny field"></div>
      <p>Mauris gravida viverra posuere. Donec semper tincidunt gravida. Cum sociis natoque penatibus et magnis dis parturient montes, nascetur ridiculus mus. Curabitur adipiscing tincidunt velit. Donec malesuada purus ut ipsum volutpat dictum ut sed leo.</p>
    </article>
    <article class="col about">
      <h2>About QNR</h2>
      <p class="quote">Neque porro quisquam est qui dolorem ipsum dolor sit amet</p>
      <p>Lorem ipsum dolor sit amet, consectetur adipiscing elit. Mauris gravida viverra posuere. Donec semper tincidunt gravida. Cum sociis natoque penatibus et magnis dis parturient montes, nascetur ridiculus mus. Curabitur adipiscing tincidunt velit. Donec malesuada purus ut ipsum volutpat dictum ut sed leo.</p>
    </article>
    <aside class="col news">
      <h2>News</h2>
      <div class="news-list">
        <span class="arrow up"><svg width="8" height="6" viewBox="0 0 8 6"><path d="M0 6L4 0L8 6Z" fill="#666"/></svg></span>
        <div class="item"><time>05.03.2011</time><p>Nunc id tempus ante, commodo eleifend ante ligula.</p></div>
        <div class="item"><time>04.03.2011</time><p>Donec tristique neque ut ante bibendum pellentesque.</p></div>
        <div class="item"><time>03.03.2011</time><p>Vestibulum quam elit, facilisis sit amet egestas eget.</p></div>
        <div class="item"><time>02.03.2011</time><p>Nunc id tempus ante commodo.</p></div>
        <span class="arrow down"><svg width="8" height="6" viewBox="0 0 8 6"><path d="M0 0L4 6L8 0Z" fill="#666"/></svg></span>
      </div>
    </aside>
  </section>

  <section class="partners" aria-label="Clients">
    <span class="partner"><span class="mark"></span>KORVAL</span>
    <span class="partner">ASTEN TEKSTIL</span>
    <span class="partner">NILGAZ</span>
    <span class="partner">MERAVAN</span>
    <span class="partner">CALVERA</span>
  </section>

  <footer class="footer">QNR © 2011 &nbsp;Privacy Notice &nbsp;| &nbsp;Conditions of Use</footer>
</body>
</html>
```